Extend Medium Rectangle into Halfpage and Billboard Ad Format

We have a few variations of our Medium Rectangle (300x250) that we use to build scalable online ads for local advertisers based on their images and logos which in most of the cases are very basic but still should deliver decent results in terms of overall banner look.

Based on those variations we would like to have each a Halfpage and Billboard variation to it that resembles the "look & feel" to feel like "out of one hand" and allows the local advertiser to recognize his ad across all formats.

Core of the Medium Rectangle is a carousel ad to swipe through the images and "more information" for the click-out to the landingpage. That might be great to replicate on the other banner formats but also could be done differently.

Attached the examples we have for one local customer to build ads from. Very limited but realistic.

```html
<!DOCTYPE html>
<html lang="de">
<head>
<meta charset="utf-8">
<title>Gasthof Linde – Halfpage</title>
<link rel="stylesheet" href="https://fonts.googleapis.com/css2?family=Cinzel:wght@500&family=Open+Sans:wght@600&family=PT+Serif:wght@400&display=swap">
<style>
  :root {
    --brand-red: #b50d13;
    --button-red: #7a0a0d;
    --white: #ffffff;
    --photo-dark: #3a2418;
    --photo-warm: #a86a3c;
    --plate: #f6f2ec;
  }
  html, body {
    margin: 0;
    padding: 0;
    overflow: hidden;
    background: var(--white);
  }
  .ad {
    position: relative;
    width: 1200px;
    height: 2400px;
    overflow: hidden;
    background: var(--brand-red);
  }
  .ad__photo {
    position: absolute;
    left: 0;
    top: 0;
    width: 1200px;
    height: 1320px;
    background:
      radial-gradient(ellipse 420px 300px at 620px 640px, #6b3e22 0%, #8a5430 45%, rgba(168,106,60,0) 100%),
      radial-gradient(ellipse 900px 560px at 640px 760px, var(--plate) 55%, rgba(246,242,236,0) 80%),
      linear-gradient(160deg, var(--photo-dark) 0%, #7a5a48 35%, #d9cfc6 70%, var(--plate) 100%);
  }
  .ad__shape {
    position: absolute;
    left: 0;
    top: 0;
    width: 1200px;
    height: 2400px;
  }
  .carousel-arrow {
    position: absolute;
    top: 1290px;
    width: 80px;
    height: 150px;
  }
  .carousel-arrow--prev { left: 40px; }
  .carousel-arrow--next { right: 40px; }
  .brand-name {
    position: absolute;
    left: 0;
    width: 1200px;
    top: 1500px;
    margin: 0;
    text-align: center;
    font-family: "Cinzel", serif;
    font-weight: 500;
    font-size: 180px;
    line-height: 1;
    letter-spacing: 4px;
    color: var(--white);
  }
  .headline {
    position: absolute;
    left: 0;
    width: 1200px;
    top: 1880px;
    margin: 0;
    text-align: center;
    font-family: "Open Sans", sans-serif;
    font-weight: 600;
    font-size: 88px;
    line-height: 140px;
    color: var(--white);
  }
  .cta {
    position: absolute;
    left: 312px;
    top: 2192px;
    width: 640px;
    height: 128px;
    background: var(--button-red);
    color: var(--white);
    font-family: "PT Serif", serif;
    font-size: 72px;
    line-height: 128px;
    text-align: center;
    text-decoration: none;
  }
</style>
</head>
<body>
<div class="ad">
  <div class="ad__photo" role="img" aria-label="Angerichtetes Gericht: gebratene Leber auf Brot mit Kräutern und Soße auf weißem Teller"></div>

  <svg class="ad__shape" viewBox="0 0 1200 2400" aria-hidden="true">
    <path d="M0 930 C 300 1160, 760 1320, 1200 1250 L1200 2400 L0 2400 Z" fill="var(--brand-red)"/>
    <path d="M0 930 C 300 1160, 760 1320, 1200 1250" fill="none" stroke="var(--white)" stroke-width="6" opacity="0.85"/>
  </svg>

  <svg class="carousel-arrow carousel-arrow--prev" viewBox="0 0 80 150" aria-label="Zurück">
    <polyline points="68,8 12,75 68,142" fill="none" stroke="var(--white)" stroke-width="12" opacity="0.8"/>
  </svg>
  <svg class="carousel-arrow carousel-arrow--next" viewBox="0 0 80 150" aria-label="Weiter">
    <polyline points="12,8 68,75 12,142" fill="none" stroke="var(--white)" stroke-width="12" opacity="0.8"/>
  </svg>

  <p class="brand-name">LINDE</p>

  <h1 class="headline">Neueröffnung Gasthof<br>Linde in Wiesental</h1>

  <a class="cta" href="#">Mehr erfahren</a>
</div>
</body>
</html>
```